Lotus Leaf Kitchen Road Billboard

Road Billboard I need all of this information on it
Authentic Thai Food Bangkok Style
6.5 Miles on the right
4126 Maple Ridge Rd Otto NC
828-555-4172

```html
<!DOCTYPE html>
<html lang="en">
<head>
<meta charset="utf-8">
<title>Lotus Leaf Kitchen Road Billboard</title>
<link rel="stylesheet" href="https://fonts.googleapis.com/css2?family=Poppins:wght@300;400;600;700;800&family=Great+Vibes&display=swap">
<style>
  :root {
    --ink: #0d0d0d;
    --gold: #dba827;
    --gold-deep: #8f6c1f;
    --white: #ffffff;
    --page: #f2f2f2;
    --text-dark: #1a1a1a;
  }
  * { box-sizing: border-box; margin: 0; padding: 0; }
  html, body { width: 902px; height: 1200px; overflow: hidden; background: var(--page); }
  .billboard {
    position: absolute; left: 21px; top: 385px;
    width: 860px; height: 430px;
    background: var(--ink);
    overflow: hidden;
    font-family: "Poppins", sans-serif;
    box-shadow: 0 4px 14px rgba(0,0,0,.25);
  }
  .billboard-art { position: absolute; inset: 0; width: 100%; height: 100%; }
  .brand { position: absolute; left: 18px; top: 26px; width: 210px; text-align: center; }
  .brand-dot { width: 58px; height: 58px; border-radius: 50%; background: var(--gold); margin: 0 auto 12px; }
  .brand-name { color: var(--gold); font-weight: 600; font-size: 19px; line-height: 1; }
  .headline { position: absolute; left: 22px; top: 148px; }
  .headline-lead { color: var(--gold); font-weight: 300; font-size: 60px; line-height: 1; letter-spacing: -0.5px; }
  .headline-main { color: var(--white); font-weight: 700; font-size: 88px; line-height: .9; letter-spacing: -2px; margin-top: 2px; }
  .tagline { position: absolute; left: 20px; top: 290px; display: flex; align-items: center; gap: 8px; color: var(--gold); }
  .tagline-rule { width: 36px; height: 4px; background: var(--white); }
  .tagline-city { font-weight: 700; font-size: 48px; line-height: 1; letter-spacing: -0.5px; }
  .tagline-style { font-family: "Great Vibes", cursive; font-size: 58px; line-height: 1; margin-left: -2px; margin-right: 6px; }
  .distance {
    position: absolute; left: 460px; top: 292px; width: 200px; height: 56px;
    border: 2px solid var(--white); border-radius: 28px;
    display: flex; align-items: center; gap: 10px; padding-left: 10px;
  }
  .distance-icon { width: 40px; height: 40px; flex: none; }
  .distance-text { text-align: center; line-height: 1; }
  .distance-miles { color: var(--gold); font-weight: 700; font-size: 24px; }
  .distance-side { color: var(--white); font-weight: 400; font-size: 15px; margin-top: 2px; }
  .address-strip {
    position: absolute; left: 0; top: 372px; width: 100%; height: 58px;
    background: var(--white);
    color: var(--text-dark); font-weight: 400; font-size: 31px;
    padding-left: 20px; line-height: 58px; letter-spacing: -0.3px;
  }
  .phone {
    position: absolute; left: 470px; top: 361px; right: 0; height: 69px;
    background: var(--gold); border-radius: 36px 0 0 0;
    display: flex; align-items: center; gap: 8px; padding-left: 20px;
    color: var(--text-dark); font-weight: 700; font-size: 39px; letter-spacing: -0.5px;
  }
  .phone-icon { width: 30px; height: 30px; flex: none; }
</style>
</head>
<body>
<main class="billboard">
  <svg class="billboard-art" viewBox="0 0 1545 772" preserveAspectRatio="none" aria-hidden="false">
    <defs>
      <radialGradient id="wok-glow" cx="0.55" cy="0.45" r="0.6">
        <stop offset="0" stop-color="#7a5a3a"/>
        <stop offset="0.35" stop-color="#b4471c"/>
        <stop offset="0.7" stop-color="#2a2320"/>
        <stop offset="1" stop-color="#121212"/>
      </radialGradient>
    </defs>
    <path class="gold-band-deep" d="M560,0 C640,300 960,520 1545,540 L1545,600 C960,600 620,380 560,0 Z" fill="#8f6c1f"/>
    <path class="gold-band" d="M560,0 C630,260 930,480 1545,470 L1545,545 C950,540 640,330 560,0 Z" fill="#dba827"/>
    <path class="food-photo" role="img" aria-label="Photo of a wok tossing shrimp, broccoli and vegetables over bright flames"
          d="M575,0 C650,230 940,440 1545,445 L1545,0 Z" fill="url(#wok-glow)"/>
  </svg>

  <div class="brand">
    <div class="brand-dot"></div>
    <p class="brand-name">Lotus Leaf Kitchen</p>
  </div>

  <h1 class="headline">
    <span class="headline-lead">Authentic</span><br>
    <span class="headline-main">Thai Food</span>
  </h1>

  <p class="tagline">
    <span class="tagline-rule"></span>
    <span class="tagline-city">Bangkok</span>
    <span class="tagline-style">Style</span>
    <span class="tagline-rule"></span>
  </p>

  <div class="distance">
    <svg class="distance-icon" viewBox="0 0 40 40">
      <circle cx="20" cy="20" r="19" fill="#ffffff"/>
      <circle cx="20" cy="20" r="16" fill="#dba827"/>
      <path d="M14,11 L28,20 L14,29 L18,20 Z" fill="#ffffff"/>
    </svg>
    <div class="distance-text">
      <p class="distance-miles">6.5 Miles</p>
      <p class="distance-side">On The Right</p>
    </div>
  </div>

  <p class="address-strip">4126 Maple Ridge Rd Otto NC</p>

  <p class="phone">
    <svg class="phone-icon" viewBox="0 0 24 24">
      <path d="M6.6 10.8a15.1 15.1 0 0 0 6.6 6.6l2.2-2.2a1 1 0 0 1 1-.25 11.4 11.4 0 0 0 3.6.57 1 1 0 0 1 1 1V20a1 1 0 0 1-1 1A17 17 0 0 1 3 4a1 1 0 0 1 1-1h3.5a1 1 0 0 1 1 1c0 1.25.2 2.45.57 3.57a1 1 0 0 1-.25 1z" fill="#1a1a1a"/>
      <path d="M15 3a6 6 0 0 1 6 6M15 6.5A2.5 2.5 0 0 1 17.5 9" stroke="#1a1a1a" stroke-width="1.8" fill="none" stroke-linecap="round"/>
    </svg>
    828-555-4172
  </p>
</main>
</body>
</html>
```